Design a label for a range of honey under :BRIGHT MEADOW HONEY. (Original quirky different)

Create a label for a range of honey products under the brand BRIGHT MEADOW HONEY.
Iam the beekeeper and want to sell for the local New Zealand market directly to the consumer, online mainly.
Brand position: A contemporary honey, a fresh look for a simple product, like nature intended, nothing taken out, nothing added. Doesnt take itself seriously.
Personality: Contemporary, fresh, modern, free and fun,loving. Doesnt take itself seriously, loving, generous, upbeat, provide enjoyment, life ...
Brand value: Straight up, keep it simple, generous, different,
Label: Modern twist of nature and goodness (no straight picture of nature) quirky?, use of slogan? ( Nature in a pot / More than just honey / Taste of nature / It's all good...
Need to stand out, make you smile, be noticed, different...

Target Market(s)

Online direct customer.

Requirements
Must have
• legal requirements for NZ labeling attached.
A twist and quirky side...
Should not have
• Basic picture of nature.
Straight forward boring everybody else's feel.

```html
<!DOCTYPE html>
<html lang="en">
<head>
<meta charset="utf-8">
<title>Bright Meadow Honey – Label Range</title>
<link href="https://fonts.googleapis.com/css2?family=Barlow+Condensed:wght@800&family=Caveat:wght@600&family=Caveat+Brush&display=swap" rel="stylesheet">
<style>
  :root {
    --honey: #fdb515;
    --ink: #231f20;
    --ink-soft: #2e2a2b;
    --paper: #ffffff;
  }
  * { margin: 0; padding: 0; box-sizing: border-box; }
  html, body { width: 1200px; height: 544px; overflow: hidden; background: var(--paper); }
  .canvas { position: relative; width: 1200px; height: 544px; }

  .label { position: absolute; color: var(--ink); }
  .label svg.shape { position: absolute; inset: 0; }
  .label--square { left: 150px; top: 112px; width: 270px; height: 300px; }
  .label--flower { left: 478px; top: 92px; width: 262px; height: 330px; }

  .lid { position: absolute; left: 842px; top: 122px; width: 302px; height: 302px; border-radius: 50%; background: var(--ink); overflow: hidden; }
  .lid__flight {
    position: absolute; left: 40px; top: 24px; width: 240px; height: 262px;
    border-radius: 50%;
    background: radial-gradient(ellipse at 60% 45%, var(--ink-soft) 0%, var(--ink) 70%);
  }

  .tagline {
    position: absolute; left: 0; right: 0; text-align: center;
    font: 600 15px/1 "Caveat", cursive; letter-spacing: 1px;
  }
  .brand {
    position: absolute; left: 0; right: 0; text-align: center;
    font: 800 25px/0.95 "Barlow Condensed", sans-serif; letter-spacing: 0.5px;
    text-transform: uppercase;
  }
  .brand--lid { color: var(--paper); font-size: 31px; top: 108px; }
  .natural {
    position: absolute; font: 600 19px/0.85 "Caveat", cursive; text-align: center;
    transform: rotate(-14deg);
  }
  .product {
    position: absolute; left: 0; right: 0; text-align: center;
    font: 400 50px/1 "Caveat Brush", cursive; letter-spacing: 2px;
  }
  .weight {
    position: absolute; left: 0; right: 0; text-align: center;
    font: 800 12px/1 "Barlow Condensed", sans-serif; letter-spacing: 0.5px;
  }
  .path-note {
    position: absolute; font: 600 11px/1 "Caveat", cursive; letter-spacing: 1px;
    transform-origin: left top; white-space: nowrap;
  }
  .bee {
    position: absolute; width: 14px; height: 10px; border-radius: 50%;
    background: var(--ink);
  }
</style>
</head>
<body>
<main class="canvas">

  <section class="label label--square">
    <svg class="shape" width="270" height="300" viewBox="0 0 270 300">
      <rect x="0" y="0" width="270" height="300" rx="24" fill="var(--honey)"/>
      <path d="M46 96 C 20 110, 24 150, 26 180 C 28 220, 22 250, 36 268"
            fill="none" stroke="var(--ink)" stroke-width="1.6" stroke-dasharray="3 4"/>
    </svg>
    <div class="bee" role="img" aria-label="Small bee illustration" style="left:48px; top:90px;"></div>
    <p class="path-note" style="left:18px; top:250px; transform: rotate(-84deg);">raw · pure · local</p>
    <p class="tagline" style="top:38px;">taste of nature</p>
    <p class="brand" style="top:64px;">Bright<br>Meadow<br>Honey</p>
    <p class="natural" style="left:190px; top:118px;">100%<br>natural</p>
    <p class="product" style="top:178px;">HONEY</p>
    <p class="weight" style="top:252px;">500 g</p>
  </section>

  <section class="label label--flower">
    <svg class="shape" width="262" height="330" viewBox="0 0 262 330">
      <g fill="var(--honey)">
        <circle cx="131" cy="70" r="66"/>
        <circle cx="62" cy="128" r="58"/>
        <circle cx="200" cy="128" r="58"/>
        <circle cx="58" cy="230" r="56"/>
        <circle cx="204" cy="230" r="56"/>
        <circle cx="131" cy="268" r="60"/>
        <rect x="40" y="80" width="182" height="200"/>
      </g>
      <path d="M54 118 C 26 140, 30 180, 40 210 C 50 240, 56 262, 80 286"
            fill="none" stroke="var(--ink)" stroke-width="1.6" stroke-dasharray="3 4"/>
    </svg>
    <div class="bee" role="img" aria-label="Small bee illustration" style="left:56px; top:110px;"></div>
    <p class="path-note" style="left:24px; top:226px; transform: rotate(-72deg);">from hive to home</p>
    <p class="tagline" style="top:28px;">taste of nature</p>
    <p class="brand" style="top:54px;">Bright<br>Meadow<br>Honey</p>
    <p class="natural" style="left:188px; top:118px;">100%<br>natural</p>
    <p class="product" style="top:190px;">HONEY</p>
    <p class="weight" style="top:266px;">500 g</p>
  </section>

  <section class="lid">
    <div class="lid__flight" role="img" aria-label="Bee with a dotted looping flight path circling the lid"></div>
    <p class="brand brand--lid">Bright<br>Meadow<br>Honey</p>
  </section>

</main>
</body>
</html>
```